Business Card & Stationary
for Dental office
Professional
Ritika Dhulekar, DDS
18467 E Larchmont Rd
Northvale, MI 48372
toothclinic@mailbrook.com
PineLedgeDental.com
Logo has business name.
Back of business card will be used for pre-printed appointment information.
Business logo on Gray color
Business Logo
Sample back of card

```html
<!DOCTYPE html>
<html lang="en">
<head>
<meta charset="utf-8">
<title>Pine Ledge Dental – Business Card</title>
<link rel="stylesheet" href="https://fonts.googleapis.com/css2?family=Tinos:wght@400;700&family=Cormorant+SC:wght@500&display=swap">
<style>
  :root {
    --page-gray: #c9cacc;
    --card-white: #f7f8fa;
    --navy: #1b2f6e;
    --brand-blue: #1d4596;
    --sky-blue: #3a8fd8;
    --band-dark: #1554b8;
    --band-light: #52a8ea;
    --band-edge: #a9d3f3;
    --ink: #2a3550;
    --rule: #8a94aa;
  }
  * { margin: 0; padding: 0; box-sizing: border-box; }
  html, body { width: 1200px; height: 919px; overflow: hidden; }
  body { background: var(--page-gray); font-family: "Tinos", "Times New Roman", serif; color: var(--ink); position: relative; }

  .card {
    position: absolute; left: 281px; width: 638px; height: 363px;
    background: var(--card-white); border-radius: 14px; overflow: hidden;
  }
  .card--front { top: 92px; }
  .card--back { top: 474px; }
  .card__band { position: absolute; left: 0; top: 0; width: 638px; height: 363px; }

  .brand-name {
    position: absolute; top: 78px; width: 100%; text-align: center;
    font-weight: 700; font-size: 50px; letter-spacing: 2px; color: var(--brand-blue);
  }
  .brand-tagline {
    position: absolute; top: 158px; width: 100%; text-align: center;
    font-family: "Cormorant SC", serif; font-weight: 500; font-size: 29px; letter-spacing: 1.5px;
    color: var(--sky-blue);
  }
  .doctor-name {
    position: absolute; left: 24px; top: 220px;
    font-weight: 700; font-size: 25px; color: var(--navy);
  }
  .contact-list { position: absolute; left: 420px; top: 232px; list-style: none; font-size: 13.5px; line-height: 17px; color: var(--ink); }
  .contact-list li { display: flex; align-items: flex-start; gap: 8px; }
  .contact-list svg { width: 12px; height: 12px; margin-top: 2px; flex: none; fill: var(--navy); }
  .contact-list .indent { padding-left: 20px; }
  .web-address {
    position: absolute; bottom: 10px; width: 100%; text-align: center;
    font-size: 14px; color: #fff;
  }

  .appt-title { position: absolute; top: 40px; width: 100%; text-align: center; font-weight: 700; font-size: 23px; color: var(--navy); }
  .faint-name {
    position: absolute; top: 118px; width: 100%; text-align: center;
    font-weight: 700; font-size: 50px; letter-spacing: 2px; color: rgba(29,69,150,0.06);
  }
  .field { position: absolute; font-size: 17px; display: flex; align-items: flex-end; gap: 6px; }
  .field__line { border-bottom: 1px solid var(--rule); height: 1px; }
  .field--for { left: 62px; top: 82px; }
  .days { position: absolute; left: 62px; top: 144px; display: flex; gap: 20px; font-size: 17px; list-style: none; }
  .days li { display: flex; align-items: center; gap: 3px; }
  .checkbox { width: 12px; height: 12px; border: 1px solid var(--ink); display: inline-block; }
  .field--date { left: 62px; top: 194px; }
  .field--time { left: 350px; top: 194px; }
  .notice { position: absolute; top: 250px; width: 100%; text-align: center; font-size: 16.5px; line-height: 21px; }
</style>
</head>
<body>

<section class="card card--front" aria-label="Business card front">
  <svg class="card__band" viewBox="0 0 638 363" aria-hidden="true">
    <defs>
      <linearGradient id="bandFront" x1="0" y1="0" x2="1" y2="0">
        <stop offset="0" stop-color="var(--band-light)"/>
        <stop offset="1" stop-color="var(--band-dark)"/>
      </linearGradient>
    </defs>
    <path d="M0,248 C120,325 360,342 638,312 L638,363 L0,363 Z" fill="var(--band-edge)"/>
    <path d="M0,262 C130,335 380,346 638,322 L638,363 L0,363 Z" fill="url(#bandFront)"/>
  </svg>
  <div class="brand-name">PINE LEDGE DENTAL</div>
  <div class="brand-tagline">Family &amp; Cosmetic Dentistry</div>
  <div class="doctor-name">Ritika Dhulekar, DDS</div>
  <ul class="contact-list">
    <li><svg viewBox="0 0 12 12"><path d="M6 1 L11 6 H9.5 V11 H2.5 V6 H1 Z"/></svg>18467 E Larchmont Rd</li>
    <li class="indent">Northvale, MI 48372</li>
    <li><svg viewBox="0 0 12 12"><path d="M2 1h3l1 3-2 1c1 2 2 3 3 3l1-2 3 1v3c-6 0-9-3-9-9z"/></svg>(734) 555-0142</li>
    <li><svg viewBox="0 0 12 12"><path d="M1 2h10v8H1z M2 3l4 3 4-3" fill="none" stroke="var(--navy)" stroke-width="1"/></svg>toothclinic@mailbrook.com</li>
  </ul>
  <div class="web-address">PineLedgeDental.com</div>
</section>

<section class="card card--back" aria-label="Appointment card back">
  <svg class="card__band" viewBox="0 0 638 363" aria-hidden="true">
    <defs>
      <linearGradient id="bandBack" x1="0" y1="0" x2="1" y2="0">
        <stop offset="0" stop-color="var(--band-light)"/>
        <stop offset="1" stop-color="var(--band-dark)"/>
      </linearGradient>
    </defs>
    <path d="M0,212 C90,312 330,340 638,318 L638,363 L0,363 Z" fill="var(--band-edge)"/>
    <path d="M0,224 C100,322 340,346 638,326 L638,363 L0,363 Z" fill="url(#bandBack)"/>
  </svg>
  <div class="faint-name" aria-hidden="true">PINE LEDGE DENTAL</div>
  <div class="appt-title">Dentis Appointment</div>
  <div class="field field--for">For <span class="field__line" style="width:500px"></span></div>
  <ul class="days">
    <li><span class="checkbox"></span>Mon</li>
    <li><span class="checkbox"></span>Tue</li>
    <li><span class="checkbox"></span>Wed</li>
    <li><span class="checkbox"></span>Thu</li>
    <li><span class="checkbox"></span>Fri</li>
    <li><span class="checkbox"></span>Sat</li>
    <li><span class="checkbox"></span></li>
  </ul>
  <div class="field field--date">Date <span class="field__line" style="width:240px"></span></div>
  <div class="field field--time">Time <span class="field__line" style="width:180px"></span></div>
  <p class="notice">If unable to keep your appointment, kindly give 24 hours notice<br>(734) 555-0142</p>
  <div class="web-address">PineLedgeDental.com</div>
</section>

</body>
</html>
```